Save the date for wedding

A save the date for our wedding. We're looking for a simple and sleek invite. I would prefer not alot of calligraphy. Minimalism is good. The basic info to include is as follows:
Names: Mona and Felix
Date: June 9th
Where: Ottawa, Ontario
In small print please include that there will be a reception in Edmonton AB September 1st for those who cannot make it to Ottawa.
Please see the attached file for a style idea. Doesn’t have to be exactly like that, but something like that.

```html
<!DOCTYPE html>
<html lang="en">
<head>
<meta charset="utf-8">
<title>Save the Date – Mona &amp; Felix</title>
<link rel="stylesheet" href="https://fonts.googleapis.com/css2?family=Kaushan+Script&family=Montserrat:wght@400&family=Libre+Baskerville:wght@700&family=Great+Vibes&family=Roboto:wght@400&display=swap">
<style>
  :root {
    --card-bg: #111111;
    --ink: #ffffff;
  }
  html, body {
    margin: 0;
    padding: 0;
    width: 1200px;
    height: 1200px;
    overflow: hidden;
    background: var(--card-bg);
  }
  .save-the-date-card {
    position: relative;
    width: 1200px;
    height: 1200px;
    background: var(--card-bg);
    color: var(--ink);
    text-align: center;
  }
  .headline {
    position: absolute;
    top: 150px;
    left: 0;
    width: 100%;
    margin: 0;
    font-family: "Kaushan Script", cursive;
    font-weight: 400;
    font-size: 170px;
    line-height: 1;
    letter-spacing: -2px;
    transform: rotate(2deg);
  }
  .headline .small-word {
    font-size: 105px;
    vertical-align: 28px;
  }
  .event-date {
    position: absolute;
    top: 510px;
    left: 0;
    width: 100%;
    margin: 0;
    font-family: "Montserrat", sans-serif;
    font-weight: 400;
    font-size: 48px;
    letter-spacing: 1px;
  }
  .event-place {
    position: absolute;
    top: 592px;
    left: 0;
    width: 100%;
    margin: 0;
    font-family: "Montserrat", sans-serif;
    font-weight: 400;
    font-size: 50px;
    letter-spacing: 2px;
    display: flex;
    justify-content: center;
    align-items: center;
    gap: 12px;
  }
  .pin-icon {
    width: 26px;
    height: 36px;
    fill: var(--ink);
  }
  .intro-line {
    position: absolute;
    top: 690px;
    left: 0;
    width: 100%;
    margin: 0;
    font-family: "Libre Baskerville", serif;
    font-weight: 700;
    font-size: 33px;
  }
  .couple-names {
    position: absolute;
    top: 800px;
    left: 100px;
    width: 1000px;
    margin: 0;
    font-family: "Great Vibes", cursive;
    font-weight: 400;
    font-size: 170px;
    line-height: 1.1;
  }
  .couple-names .ampersand {
    font-size: 110px;
    padding: 0 40px;
  }
  .fine-print {
    position: absolute;
    top: 1122px;
    left: 0;
    width: 100%;
    margin: 0;
    font-family: "Roboto", sans-serif;
    font-weight: 400;
    font-size: 19px;
  }
</style>
</head>
<body>
  <main class="save-the-date-card">
    <h1 class="headline">Save <span class="small-word">the</span> Date</h1>
    <p class="event-date">Saturday, June 9th, 2018</p>
    <p class="event-place">
      <svg class="pin-icon" viewBox="0 0 26 36" aria-hidden="true">
        <path d="M13 0C5.8 0 0 5.8 0 13c0 9.2 13 23 13 23s13-13.8 13-23C26 5.8 20.2 0 13 0zm0 18a5 5 0 1 1 0-10 5 5 0 0 1 0 10z"/>
      </svg>
      <span>Ottawa, Ontario</span>
    </p>
    <p class="intro-line">For the Wedding Celebration of</p>
    <h2 class="couple-names">Mona<span class="ampersand">&amp;</span>Felix</h2>
    <p class="fine-print">There will be a reception in Edmonton AB September 1st for those who cannot make it to Ottawa.</p>
  </main>
</body>
</html>
```